Steadfast MD - Sleep Medicine Specialist - Business Cards

We are a new medical practice called Steadfast MD. We are sleep medicine specialists and we will be conducting sleep studies on patients with sleep related ailments. We want the business card to be bold, professional, and clean with the logo as the stand out visual piece. We dont like wild flashy designs. We want our design to be bold and classic while at the same time conveying who we are and what we do. We are reliable, professional, and the best in the business.

Industry/Entity Type

Health Care

Contact Information for Business Card

- Clean
- Bold
- Classic
- not cluttered

Requirements
Must have
• logo, website, phone number
Nice to have
• several options to choose from
Should not have
• flashy imaged - reflective print - images of people sleeping

```html
<!DOCTYPE html>
<html lang="en">
<head>
<meta charset="utf-8">
<title>Steadfast MD – Business Cards</title>
<link rel="stylesheet" href="https://fonts.googleapis.com/css2?family=Inter:wght@400;700;800&display=swap">
<style>
  :root {
    --backdrop: #e2e2e2;
    --card-dark: #060608;
    --card-light: #f4f4f4;
    --brand-red: #e31e24;
    --ink: #111111;
    --paper-white: #ffffff;
  }
  * { margin: 0; padding: 0; box-sizing: border-box; }
  html, body {
    width: 1200px;
    height: 960px;
    overflow: hidden;
  }
  body {
    position: relative;
    background: var(--backdrop);
    font-family: "Inter", Arial, sans-serif;
    color: var(--ink);
  }
  .card {
    position: absolute;
    left: 297px;
    width: 606px;
    height: 346px;
    overflow: hidden;
    box-shadow: 3px 4px 6px rgba(0, 0, 0, 0.35);
  }
  .card--front { top: 116px; background: var(--card-dark); }
  .card--back  { top: 516px; background: var(--card-light); }

  .front-ring {
    position: absolute;
    left: 298px;
    top: -4px;
    width: 320px;
    height: 320px;
    border: 10px solid var(--brand-red);
    border-radius: 50%;
  }
  .front-name {
    position: absolute;
    left: 53px;
    top: 262px;
    font-size: 40px;
    font-weight: 800;
    letter-spacing: -1px;
    color: var(--paper-white);
    white-space: nowrap;
  }

  .back-brand {
    position: absolute;
    left: 47px;
    top: 145px;
    display: flex;
    align-items: center;
    gap: 6px;
  }
  .back-brand__dot {
    width: 58px;
    height: 58px;
    border: 3px solid var(--brand-red);
    border-radius: 50%;
  }
  .back-brand__name {
    font-size: 26px;
    font-weight: 800;
    letter-spacing: -0.6px;
    color: var(--ink);
    white-space: nowrap;
  }
  .divider {
    position: absolute;
    left: 302px;
    top: 108px;
    width: 2px;
    height: 128px;
    background: var(--ink);
  }
  .contact {
    position: absolute;
    left: 335px;
    top: 109px;
  }
  .contact__name {
    font-size: 19px;
    font-weight: 700;
    color: var(--brand-red);
    letter-spacing: 0.6px;
    line-height: 22px;
  }
  .contact__role {
    font-size: 15px;
    line-height: 20px;
    margin-bottom: 20px;
  }
  .contact__list { list-style: none; }
  .contact__item {
    display: flex;
    align-items: center;
    gap: 6px;
    font-size: 15px;
    line-height: 20px;
  }
  .contact__icon { width: 13px; height: 13px; fill: var(--brand-red); flex: none; }
</style>
</head>
<body>
  <section class="card card--front">
    <div class="front-ring"></div>
    <div class="front-name">Steadfast MD</div>
  </section>

  <section class="card card--back">
    <div class="back-brand">
      <div class="back-brand__dot"></div>
      <div class="back-brand__name">Steadfast MD</div>
    </div>
    <div class="divider"></div>
    <div class="contact">
      <div class="contact__name">DANIEL CARTER</div>
      <div class="contact__role">Managing Director</div>
      <ul class="contact__list">
        <li class="contact__item">
          <svg class="contact__icon" viewBox="0 0 16 16" aria-hidden="true"><path d="M3.6 1.2l2.3 2.6c.4.4.3 1-.1 1.4L4.6 6.3c.9 2 2.6 3.8 4.8 4.9l1.1-1.2c.4-.4 1-.5 1.4-.1l2.6 2.3c.4.4.4 1 0 1.4l-1.4 1.3c-.6.6-1.6.7-2.4.3C6 13.3 2.8 10 .9 5.3.6 4.5.7 3.6 1.3 3l1.3-1.6c.3-.5.7-.5 1-.2z"/></svg>
          (123) 456-7890
        </li>
        <li class="contact__item">
          <svg class="contact__icon" viewBox="0 0 16 16" aria-hidden="true"><path d="M1 3h14v10H1z M2.5 4.5v.3L8 9l5.5-4.2v-.3z M2.5 6.6v5h11v-5L8 10.8z" fill-rule="evenodd"/></svg>
          daniel@steadfastmd.com
        </li>
        <li class="contact__item">
          <svg class="contact__icon" viewBox="0 0 16 16" aria-hidden="true"><path fill="none" stroke="#e31e24" stroke-width="1.3" d="M8 1.2a6.8 6.8 0 1 0 0 13.6A6.8 6.8 0 1 0 8 1.2zM1.2 8h13.6M8 1.2c-2.4 2-2.4 11.6 0 13.6M8 1.2c2.4 2 2.4 11.6 0 13.6M2.3 4.6h11.4M2.3 11.4h11.4"/></svg>
          www.steadfastmd.com
        </li>
      </ul>
    </div>
  </section>
</body>
</html>
```